New Toothpaste brand needs a logo & packaging design

Our company is launching a new toothpaste and is looking for a logo and packaging design. The toothpaste brand is called Brivana. The packaging should have the same design quality as the major international brands, such as Lumora, Lumora Totalcare, Dentiva, Pexolo, Wind-rise, Marvest, etc. The dominant colors for our brand should be hues of blue, similar to other major brands. In addition, there should be a little bit of green to represent the "Fresh Mint Blast" flavor and the "Extracts of Aloe Vera" included in the ingredients.

There are typically 3 unique sides on a toothpaste box:

The face: Repeated on ~3 sides of the 4 faces of the box
The back: The 4th box face has the instructions for use, ingredients, company information, bar code/product info, and some branding elements.
The sides: Usually consisting of just the logo, flavor etc.

Please refer to existing brands such as Lumora, Lumora Total-care, and Dentiva for an example of typical box layout and elements.

Task Details:
Package Dimensions: 180 mm x 48 mm x 28 mm, 100 ml toothpaste tube
Brand Name: Brivana
Description: Fluoride Toothpaste
Flavor: Fresh Mint Blast
5 Actions: Protects against cavities and tartar, freshens breath, whitens teeth, and maintains healthy gums. These actions can also be made into a list like Lumora Total Care or Dentiva Max care. For instance, Strong Teeth, Fresh Breath, Whitening, Healthy Gums, Cavity and Tartar Protection.
Also contains whitening micro particles and extracts of aloe vera which may be highlighted on the package

Overall, the look should be high quality and with the same look and feel as the big brands mentioned previously. We do not have an existing logo for this brand. The face of the package is the most important element as it is often repeated on several sides and on the tube itself.

Please let me know if you have any questions.

I've attached some of our favorite big brand designs below. I would say the Lumora Total Care and Gleam vers

The logos I've seen so far for Brivana, have been a bit too bold. A little bold is okay, but just needs to be moderate. 

I would like the colors to be bright and appealing. I mentioned shades of blue being the major color, but green should also be highlighted as well, perhaps in a 80% blue to 20% green ratio. 

Target Market(s)

adult consumer of toothpaste, both female and male.

Industry/Entity Type

It Company

Requirements
Must have
• A logo with the brand name: Brivana
Description or sub text: Fluoride Toothpaste
Flavor: Fresh Mint Blast
A phrase or list describing the Toothpaste Actions: e.g., Protects against cavities and tartar, freshens breath, whitens teeth, and maintains healthy gums. Or as a list simialr to Lumora Total Care or Dentiva Max Care:
-Anti-cavity
-Anti-tartar
-Fresh breath
-Whitening
-Healthy Gums

Special ingredient of "whitening micro particles: and "extracts of aloe vera", which should also be highlighted.

The color should mostly be shades of blue, with only a little bit of green to accentuate the fresh mint blast flavor and aloe vera

Nice to have
• The design should really look good next to lumora total care, gleam pure, and dentiva max care. These are our favorite designs.
Should not have
• For aloe vera, there is no need to show the plant.

The Brivana logo shouldn't be too Bold. This should be appeal to all consumers, not just men.

```html
<!DOCTYPE html>
<html lang="en">
<head>
<meta charset="utf-8">
<title>Brivana Fluoride Toothpaste – Packaging Face and Logo</title>
<link rel="stylesheet" href="https://fonts.googleapis.com/css2?family=Open+Sans:wght@600;700;800&display=swap">
<style>
  :root {
    --canvas-bg: #f3f4f6;
    --navy-deep: #14237a;
    --navy: #1d3594;
    --blue-glow: #3f7fe0;
    --blue-logo: #2a56b0;
    --green: #2aa84a;
    --green-light: #5fd06e;
    --green-pale: #bfeec3;
    --white: #ffffff;
  }
  * { margin: 0; padding: 0; box-sizing: border-box; }
  html, body {
    width: 1200px;
    height: 900px;
    overflow: hidden;
    background: var(--canvas-bg);
    font-family: "Open Sans", Arial, sans-serif;
  }
  .canvas {
    position: relative;
    width: 1200px;
    height: 900px;
  }
  .pack-face {
    position: absolute;
    left: 100px;
    top: 200px;
    width: 1000px;
    height: 265px;
    overflow: hidden;
    box-shadow: 0 6px 20px rgba(20, 35, 122, 0.18);
  }
  .pack-face__bg {
    position: absolute;
    inset: 0;
    width: 100%;
    height: 100%;
  }
  .brand-name {
    position: absolute;
    left: 110px;
    top: 22px;
    font-size: 92px;
    font-weight: 700;
    letter-spacing: -1px;
    color: var(--white);
    line-height: 1.1;
  }
  .product-type {
    position: absolute;
    left: 60px;
    top: 164px;
    font-size: 30px;
    font-weight: 800;
    color: var(--white);
    letter-spacing: 0.5px;
  }
  .flavor-badge {
    position: absolute;
    left: 468px;
    top: 170px;
    padding: 4px 12px;
    background: var(--green);
    border-radius: 4px;
    font-size: 14px;
    font-weight: 700;
    color: var(--white);
    letter-spacing: 0.5px;
  }
  .benefit-list {
    position: absolute;
    left: 60px;
    top: 226px;
    font-size: 12.5px;
    font-weight: 600;
    color: var(--white);
    letter-spacing: 0.4px;
    white-space: nowrap;
  }
  .ingredient-claim {
    position: absolute;
    left: 770px;
    top: 28px;
    width: 210px;
    font-size: 18px;
    font-weight: 800;
    line-height: 1.2;
    color: var(--white);
  }
  .aloe-art {
    position: absolute;
    left: 870px;
    top: 130px;
    width: 120px;
    height: 135px;
    background: linear-gradient(160deg, rgba(191, 238, 195, 0.0) 0%, rgba(191, 238, 195, 0.55) 60%, rgba(95, 208, 110, 0.6) 100%);
  }
  .drop-badge {
    position: absolute;
    left: 786px;
    top: 160px;
    width: 64px;
    height: 64px;
  }
  .brand-mark {
    position: absolute;
    left: 0;
    top: 560px;
    width: 1200px;
    text-align: center;
    font-size: 110px;
    font-weight: 700;
    letter-spacing: -1px;
    color: var(--blue-logo);
  }
</style>
</head>
<body>
<main class="canvas">
  <section class="pack-face" aria-label="Brivana toothpaste box face">
    <svg class="pack-face__bg" viewBox="0 0 1000 265" preserveAspectRatio="none" aria-hidden="true">
      <defs>
        <radialGradient id="blue-field" cx="0.3" cy="0.35" r="0.7">
          <stop offset="0" stop-color="#3f7fe0"/>
          <stop offset="0.45" stop-color="#1d3594"/>
          <stop offset="1" stop-color="#14237a"/>
        </radialGradient>
        <linearGradient id="green-field" x1="0" y1="0" x2="1" y2="1">
          <stop offset="0" stop-color="#2aa84a"/>
          <stop offset="1" stop-color="#5fd06e"/>
        </linearGradient>
      </defs>
      <rect width="1000" height="265" fill="url(#green-field)"/>
      <path d="M0 0 H680 C735 70 750 170 710 265 H0 Z" fill="#ffffff"/>
      <path d="M0 0 H660 C712 70 726 170 688 265 H0 Z" fill="url(#blue-field)"/>
    </svg>

    <div class="brand-name">Brivana</div>
    <div class="product-type">FLUORIDE TOOTHPASTE</div>
    <div class="flavor-badge">FRESH MINT BLAST</div>
    <div class="benefit-list">STRONG TEETH · FRESH BREATH · WHITENING · HEALTHY GUMS · CAVITY AND TARTAR PROTECTION</div>

    <p class="ingredient-claim">CONTAINS WHITENING MICRO PARTICLES AND EXTRACTS OF ALOE VERA</p>
    <div class="aloe-art" role="img" aria-label="Soft green aloe vera leaf artwork"></div>
    <svg class="drop-badge" viewBox="0 0 64 64" aria-hidden="true">
      <circle cx="32" cy="32" r="30" fill="#ffffff"/>
      <circle cx="32" cy="32" r="24" fill="#dff5e1"/>
      <path d="M32 16 C38 26 43 32 43 38 A11 11 0 0 1 21 38 C21 32 26 26 32 16 Z" fill="#2aa84a"/>
    </svg>
  </section>

  <div class="brand-mark">Brivana</div>
</main>
</body>
</html>
```